Design some Business Cards

We are a Photography and Social Media company that takes pictures for business and individuals and creates Lumigrove, Glimmerdot, Quillo etc. We need a very creative business card that has our logo. We will be getting our business cards from kestrel ink. We don't have a set location yet so the address can be 478 fernwood lane Brooklyn NY 11987. phone number xxx-xxx-xxxx

Please find our logo attached.

Please incorporate both logos.

Please have both logos on separate sides of the business card.

```html
<!DOCTYPE html>
<html lang="en">
<head>
<meta charset="utf-8">
<title>Bright Frame Studio – Business Cards</title>
<link href="https://fonts.googleapis.com/css2?family=Josefin+Sans:wght@300&family=Tinos&display=swap" rel="stylesheet">
<style>
  :root {
    --backdrop: #e6e4e1;
    --ink-dark: #2a2a2b;
    --ink-mid: #4a4a4b;
    --panel-grey: #bdbdbd;
    --panel-light: #f1f1f1;
    --logo-ink: #3a3a3a;
    --contact-ink: #f2f2f2;
  }
  * { margin: 0; padding: 0; box-sizing: border-box; }
  html, body { width: 1200px; height: 900px; overflow: hidden; background: var(--backdrop); }
  .canvas { position: relative; width: 1200px; height: 900px; }
  .card {
    position: absolute; width: 700px; height: 400px; overflow: hidden;
    box-shadow: 0 10px 28px rgba(0,0,0,.25);
  }
  .card--front { left: 70px; top: 50px; }
  .card--back { left: 430px; top: 470px; }
  .card-shapes { position: absolute; inset: 0; width: 100%; height: 100%; }
  .wordmark {
    position: absolute; font-family: "Josefin Sans", sans-serif; font-weight: 300;
    color: var(--logo-ink); text-transform: uppercase; font-size: 38px;
    letter-spacing: 0.42em; line-height: 1.35;
  }
  .wordmark span { display: block; }
  .wordmark span:nth-child(2) { margin-left: 0.3em; }
  .wordmark span:nth-child(3) { margin-left: 1.6em; }
  .card--front .wordmark { left: 210px; top: 95px; }
  .card--back .wordmark { left: 70px; top: 120px; font-size: 34px; }
  .social-row {
    position: absolute; left: 60px; bottom: 38px; display: flex; gap: 34px;
    font-family: "Josefin Sans", sans-serif; font-weight: 300; font-size: 15px;
    color: var(--logo-ink); letter-spacing: 0.06em;
  }
  .contact-list {
    position: absolute; right: 26px; top: 70px; list-style: none;
    font-family: "Tinos", serif; color: var(--contact-ink); text-align: right;
    font-size: 15px; line-height: 1.25;
  }
  .contact-list li { display: flex; justify-content: flex-end; align-items: center; gap: 10px; }
  .contact-list li.indent-1 { margin-right: 10px; }
  .contact-list li.indent-2 { margin-right: 20px; }
  .contact-list svg { width: 16px; height: 16px; flex: none; }
  .address { font-size: 18px; text-align: right; margin-top: 4px; margin-right: 28px; line-height: 1.1; }
</style>
</head>
<body>
<div class="canvas">

  <section class="card card--front" aria-label="Business card front">
    <svg class="card-shapes" viewBox="0 0 700 400" preserveAspectRatio="none">
      <rect width="700" height="400" fill="var(--ink-dark)"/>
      <polygon points="50,0 600,0 700,190 700,400 130,400 0,120" fill="var(--ink-mid)"/>
      <polygon points="90,0 560,0 640,400 230,400 0,90" fill="var(--panel-grey)"/>
      <polygon points="130,0 520,0 600,400 270,400 60,130" fill="var(--panel-light)"/>
    </svg>
    <h1 class="wordmark"><span>Bright</span><span>Frame</span><span>Studio</span></h1>
  </section>

  <section class="card card--back" aria-label="Business card back">
    <svg class="card-shapes" viewBox="0 0 700 400" preserveAspectRatio="none">
      <rect width="700" height="400" fill="var(--ink-dark)"/>
      <polygon points="0,110 270,0 340,0 560,400 0,400" fill="var(--ink-mid)"/>
      <polygon points="0,150 240,40 290,40 500,400 0,400" fill="var(--panel-grey)"/>
      <polygon points="0,170 220,70 250,70 470,400 0,400" fill="var(--panel-light)"/>
    </svg>
    <h2 class="wordmark"><span>Bright</span><span>Frame</span><span>Studio</span></h2>
    <ul class="social-row">
      <li>Lumigrove</li><li>Quillo</li><li>Glimmerdot</li>
    </ul>
    <ul class="contact-list">
      <li>xxx-xxx-xxxx
        <svg viewBox="0 0 16 16"><path d="M3 2h3l1 3-2 1a8 8 0 0 0 5 5l1-2 3 1v3a1 1 0 0 1-1 1A12 12 0 0 1 2 3a1 1 0 0 1 1-1z" fill="currentColor"/></svg></li>
      <li class="indent-1">You Fax Number
        <svg viewBox="0 0 16 16"><rect x="4" y="2" width="8" height="4" fill="currentColor"/><rect x="1" y="6" width="14" height="6" rx="1" fill="currentColor"/><rect x="4" y="10" width="8" height="4" fill="var(--ink-dark)" stroke="currentColor"/></svg></li>
      <li class="indent-1">Your Mail ID
        <svg viewBox="0 0 16 16"><rect x="1" y="3" width="14" height="10" fill="currentColor"/><path d="M1 3l7 6 7-6" fill="none" stroke="var(--ink-dark)" stroke-width="1.2"/></svg></li>
      <li class="indent-2">Your WebSite
        <svg viewBox="0 0 16 16"><circle cx="8" cy="8" r="6.5" fill="none" stroke="currentColor" stroke-width="1.3"/><ellipse cx="8" cy="8" rx="2.8" ry="6.5" fill="none" stroke="currentColor"/><path d="M1.5 8h13" stroke="currentColor"/></svg></li>
      <li class="indent-2">
        <svg viewBox="0 0 16 16"><path d="M8 1a5 5 0 0 0-5 5c0 4 5 9 5 9s5-5 5-9a5 5 0 0 0-5-5z" fill="currentColor"/><circle cx="8" cy="6" r="2" fill="var(--ink-dark)"/></svg></li>
      <li class="address">478 fernwood lane Brooklyn<br>NY 11987</li>
    </ul>
  </section>

</div>
</body>
</html>
```